Esthetically Pleasing Core Values and Brand Promise for Accounting Firm

I would like a cohesive design that ties together my core values and brand promise. My firm, Maple Finch Advisory, provides accounting work to small businesses. I prefer modern and clean designs. I want my Core Values and Brand Promise to represent me - sole entrepreneur, married, mother of two kids, modern esthetics, clean lines, organized, colorful (teals, greys, white, yellows)

Industry/Entity Type

Public Accounting

Colors
33b8a4

```html
<!DOCTYPE html>
<html lang="en">
<head>
<meta charset="utf-8">
<title>Maple Finch Advisory – Brand Promise &amp; Core Values</title>
<link href="https://fonts.googleapis.com/css2?family=Montserrat:wght@200;300;500;600;700;800&family=Open+Sans:wght@400;600&display=swap" rel="stylesheet">
<style>
  :root {
    --teal: #33b8a4;
    --teal-deep: #2aa592;
    --teal-soft: #6fcbbb;
    --yellow: #f5e63a;
    --grey-text: #444a4f;
    --page-bg: #ffffff;
    --white: #ffffff;
  }
  * { margin: 0; padding: 0; box-sizing: border-box; }
  html, body { width: 1200px; height: 1000px; overflow: hidden; background: var(--page-bg); }
  body { position: relative; font-family: "Montserrat", sans-serif; }

  .flyer {
    position: absolute; left: 256px; top: 18px; width: 688px; height: 967px;
    background: var(--white); overflow: hidden;
    box-shadow: 2px 3px 8px rgba(0,0,0,0.35);
  }
  .flyer-shapes { position: absolute; inset: 0; }

  .brand-badge {
    position: absolute; left: 80px; top: 2px; width: 104px; height: 104px;
    border-radius: 50%; background: var(--white);
    display: flex; align-items: center; justify-content: center; text-align: center;
    color: var(--teal); font-weight: 500; font-size: 15px; line-height: 1.1;
  }

  .hero-title { position: absolute; left: 6px; top: 206px; width: 380px; text-align: center; color: var(--white); }
  .hero-title .name { font-weight: 800; font-size: 52px; letter-spacing: -0.5px; line-height: 1; }
  .hero-title .rule { height: 1px; background: rgba(255,255,255,0.8); margin: 16px 6px 10px; }
  .hero-title .tagline { font-weight: 200; font-size: 54px; line-height: 1; letter-spacing: 0.5px; }

  .promise { position: absolute; left: 20px; top: 532px; width: 280px; color: var(--white); text-align: center; }
  .promise h2 { font-weight: 600; font-size: 26px; letter-spacing: 0.2px; }
  .promise .subtitle { font-size: 13px; font-weight: 700; margin-top: 4px; }
  .promise .underline { width: 160px; height: 3px; background: var(--yellow); margin: 9px auto 0; }

  .service-pill {
    position: absolute; left: 49px; width: 208px; height: 36px;
    background: var(--white); border-radius: 18px 4px 18px 4px;
    color: var(--teal); font-weight: 700; font-size: 20px;
    display: flex; align-items: center; justify-content: center;
  }
  .service-text {
    position: absolute; color: var(--white);
    font-family: "Open Sans", sans-serif; font-size: 14px; line-height: 15px;
  }
  .service-tax { top: 607px; }
  .service-tax-text { left: 55px; top: 648px; width: 225px; }
  .service-acc { top: 739px; }
  .service-acc-text { left: 49px; top: 790px; width: 240px; }

  .values-title {
    position: absolute; left: 404px; top: 522px; width: 200px; text-align: center;
    color: var(--teal); font-weight: 600; font-size: 28px;
  }
  .values-title::after {
    content: ""; display: block; width: 162px; height: 3px; background: var(--yellow); margin: 4px auto 0;
  }
  .value { position: absolute; width: 140px; }
  .value h3 { color: var(--teal); font-weight: 600; font-size: 17px; margin-bottom: 8px; }
  .value p { font-family: "Open Sans", sans-serif; font-size: 12px; line-height: 14px; color: var(--grey-text); }
  .value-empower { left: 367px; top: 590px; }
  .value-empower p { padding-left: 0; }
  .value-client { left: 522px; top: 590px; width: 150px; }
  .value-rectitude { left: 364px; top: 737px; }
  .value-relentless { left: 526px; top: 737px; }
  .value-empower h3, .value-rectitude h3 { padding-left: 8px; }
  .value-client p, .value-relentless p { padding-left: 4px; }

  .contact { position: absolute; color: var(--white); }
  .contact-phone { left: 32px; top: 902px; display: flex; align-items: center; gap: 10px; }
  .contact-phone .label { font-weight: 700; font-size: 15px; line-height: 1; }
  .contact-phone .number { font-weight: 800; font-size: 25px; line-height: 1.05; }
  .contact-web { left: 254px; top: 926px; display: flex; align-items: center; gap: 6px; font-size: 13px; font-family: "Open Sans", sans-serif; }
  .contact-address { left: 460px; top: 920px; display: flex; align-items: center; gap: 12px; font-size: 12px; line-height: 13px; font-family: "Open Sans", sans-serif; }
</style>
</head>
<body>
<main class="flyer">
  <svg class="flyer-shapes" viewBox="0 0 688 967" width="688" height="967" aria-hidden="false">
    <defs>
      <linearGradient id="officeTone" x1="0" y1="0" x2="1" y2="1">
        <stop offset="0" stop-color="#d9dcdc"/>
        <stop offset="0.5" stop-color="#b7b9b6"/>
        <stop offset="1" stop-color="#e8e9e8"/>
      </linearGradient>
      <linearGradient id="cityTone" x1="0" y1="0" x2="0" y2="1">
        <stop offset="0" stop-color="#7fcfc2"/>
        <stop offset="1" stop-color="#4fbba9"/>
      </linearGradient>
      <linearGradient id="homeTone" x1="0" y1="0" x2="1" y2="1">
        <stop offset="0" stop-color="#e7e2da"/>
        <stop offset="1" stop-color="#9c8f82"/>
      </linearGradient>
    </defs>

    <path class="office-photo" role="img" aria-label="Photo of a team working together at laptops in a bright office"
          d="M250,0 H688 V380 C640,440 560,480 470,490 L250,490 Z" fill="url(#officeTone)"/>
    <path class="accent-yellow" d="M440,500 C560,495 650,450 688,360 V410 C655,475 570,512 440,500 Z" fill="var(--yellow)"/>
    <path class="accent-yellow" d="M250,0 H372 C330,10 292,34 272,62 C266,36 258,14 250,0 Z" fill="var(--yellow)"/>

    <path class="city-panel" role="img" aria-label="Teal-toned photo of a city skyline"
          d="M0,0 H270 C360,40 440,150 436,270 C432,360 380,400 320,440 C270,475 200,505 120,510 C70,512 30,505 0,500 Z" fill="url(#cityTone)"/>
    <rect x="0" y="80" width="38" height="104" fill="var(--teal)" opacity="0.8"/>

    <ellipse class="family-photo" role="img" aria-label="Photo of a mother working on a laptop at home with her two children"
             cx="348" cy="422" rx="100" ry="62" fill="url(#homeTone)" stroke="var(--white)" stroke-width="3"/>

    <path class="promise-panel" d="M0,500 C60,482 150,470 230,480 C300,490 322,530 312,600 C302,680 332,760 332,820 C332,870 300,892 260,902 L0,902 Z" fill="var(--teal)"/>

    <line x1="506" y1="602" x2="506" y2="696" stroke="#333" stroke-width="2" stroke-dasharray="2 4"/>
    <line x1="506" y1="760" x2="506" y2="818" stroke="#333" stroke-width="2" stroke-dasharray="2 4"/>
    <line x1="370" y1="710" x2="482" y2="710" stroke="#333" stroke-width="2" stroke-dasharray="2 4"/>
    <line x1="532" y1="710" x2="656" y2="710" stroke="#333" stroke-width="2" stroke-dasharray="2 4"/>

    <path class="accent-yellow" d="M420,876 C540,878 630,862 688,838 V870 C630,892 530,896 420,876 Z" fill="var(--yellow)"/>
    <path class="footer-band" d="M0,878 C150,852 400,866 688,900 V967 H0 Z" fill="var(--teal)"/>
    <path d="M0,878 C150,852 400,866 688,900" fill="none" stroke="var(--teal-deep)" stroke-width="3"/>

    <line x1="432" y1="918" x2="444" y2="944" stroke="var(--white)" stroke-width="1.5" stroke-dasharray="2 3"/>
  </svg>

  <div class="brand-badge">Maple Finch<br>Advisory</div>

  <header class="hero-title">
    <div class="name">MAPLE FINCH</div>
    <div class="rule"></div>
    <div class="tagline">ADVISORY</div>
  </header>

  <section class="promise">
    <h2>BRAND PROMISE</h2>
    <p class="subtitle">Trust, Transparency and Dependability</p>
    <div class="underline"></div>
  </section>

  <div class="service-pill service-tax">Tax</div>
  <p class="service-text service-tax-text">Maple Finch provides all clients with a trusted tax advisor who provides accuracy in all filings and ensures your compliance with all government agencies.</p>
  <div class="service-pill service-acc">Accounting</div>
  <p class="service-text service-acc-text">Maple Finch provides all business owners with the financial visibility needed to foster growth and facilitate goals.</p>

  <h2 class="values-title">Core Values</h2>
  <div class="value value-empower">
    <h3>Empower</h3>
    <p>we are dedicated, appreciative and respectful of people ’s time and purpose.</p>
  </div>
  <div class="value value-client">
    <h3>Client Focused</h3>
    <p>we provide a personal service that goes above the standards of professional care.</p>
  </div>
  <div class="value value-rectitude">
    <h3>Rectitude</h3>
    <p>we know the difference between what we have the right to do and what the right thing to do is.</p>
  </div>
  <div class="value value-relentless">
    <h3>Relentless</h3>
    <p>we believe that the longer we try to do our best, the better we become.</p>
  </div>

  <div class="contact contact-phone">
    <svg width="18" height="34" viewBox="0 0 18 34" aria-hidden="true">
      <path d="M6,2 C3,3 1,7 1,17 C1,27 3,31 6,32 L9,31 C10,30 10,27 9,24 L7,22 C6,19 6,15 7,12 L9,10 C10,7 10,4 9,3 Z" fill="var(--white)"/>
    </svg>
    <div>
      <div class="label">FOR MORE INFO</div>
      <div class="number">555.014.2290</div>
    </div>
  </div>

  <div class="contact contact-web">
    <svg width="14" height="14" viewBox="0 0 14 14" aria-hidden="true">
      <g fill="none" stroke="var(--white)" stroke-width="1.2">
        <circle cx="7" cy="7" r="6"/><ellipse cx="7" cy="7" rx="2.6" ry="6"/><line x1="1" y1="7" x2="13" y2="7"/>
      </g>
    </svg>
    <span>maplefinchadvisory.com</span>
  </div>

  <div class="contact contact-address">
    <svg width="13" height="18" viewBox="0 0 13 18" aria-hidden="true">
      <path d="M6.5,0 C3,0 0,2.7 0,6.3 C0,10.5 6.5,18 6.5,18 C6.5,18 13,10.5 13,6.3 C13,2.7 10,0 6.5,0 Z M6.5,8.8 A2.5,2.5 0 1,1 6.5,3.8 A2.5,2.5 0 1,1 6.5,8.8 Z" fill="var(--white)"/>
    </svg>
    <span>1180 W.Harbor Lane, Suite 400<br>Westbrook, California 90210</span>
  </div>
</main>
</body>
</html>
```